User-interface and web design for new forum-style communication platform

We developed a new forum-style communication platform specially targetting stock investors to share and discuss information on companies listed on the stock exchange.

You have complete freedom for designing the user-interface and web design. Designs should include all features listed below.

Please read the attached document for full specifications. Also attached is a mockup of the layout, but this is only directional. A mockup for the user-profile is also attached, but does not need to be designed.

This project focusses on the homepage and thread view.

The winner(s) will be asked to design the complete project. (create thread box, user profile, registering, settings...)

We are looking for a well thought out, smart design that incorporates the specifications in the attached document. Please do not hesitate to contact us if anything is not clear.

Target Market(s)

Stock investors from 25 to 60 years old (the people that are currently on investor forums)

Industry/Entity Type

Communication

Font styles to use
Sans Serif

Colors

Designer to choose colors to be used in the design.

Requirements
Must have
• Full homepage design & Thread view specified in the attached document.
Nice to have
• Create thread view
- Field for adding tags
- field for subject of the thread
- text box with basic text editing
- method for sharing media
Should not have
• Logo design.

```html
<!DOCTYPE html>
<html lang="en">
<head>
<meta charset="utf-8">
<title>Forum – #acmecorp</title>
<link href="https://fonts.googleapis.com/css2?family=Source+Sans+3:wght@400;600&display=swap" rel="stylesheet">
<style>
:root{
  --bar:#2b3033; --bar-line:#1e2224; --page:#efefef; --panel:#ffffff;
  --line:#dcdcdc; --text:#333; --muted:#8a8a8a; --soft:#a5a5a5;
  --link:#4a95b5; --green:#6aa526; --green-dark:#5a9020; --send:#4a92ad;
  --tab:#eef3f6; --bubble:#f6f6f6; --star:#f0b429; --badge:#f5a623;
}
*{box-sizing:border-box;margin:0;padding:0}
html,body{width:1024px;height:1200px;overflow:hidden}
body{font-family:"Source Sans 3",sans-serif;background:var(--page);color:var(--text);position:relative}
.abs{position:absolute}
/* top bar */
.topbar{left:0;top:0;width:1024px;height:56px;background:linear-gradient(#343a3d,#24292b);border-bottom:1px solid #111}
.topbar .sep{top:0;width:1px;height:56px;background:var(--bar-line);box-shadow:1px 0 0 #3b4144}
.menu{left:140px;top:22px}
.logo{left:194px;top:15px;color:#fff;font-size:20px}
.search{left:287px;top:14px;width:340px;height:27px;background:#fff;border-radius:2px;font-size:11px;color:#999;padding:6px 0 0 27px}
.search svg{position:absolute;left:9px;top:8px}
.notify{left:676px;top:20px}
.badge{left:692px;top:9px;width:15px;height:15px;border-radius:50%;background:var(--badge);color:#fff;font-size:8px;text-align:center;line-height:15px;font-weight:600}
.me-avatar{left:730px;top:13px;width:29px;height:29px;background:linear-gradient(135deg,#c9a58b,#6d5747);border:1px solid #fff}
.me-name{left:767px;top:13px;color:#fff;font-size:11.5px}
.me-mail{left:767px;top:29px;color:#6fb6d6;font-size:9px}
.caret{left:878px;top:32px}
/* sidebar */
.side{left:0;width:265px;background:var(--panel);border:1px solid var(--line);border-left:0}
.side-top{top:96px;height:224px}
.side-feed{top:331px;height:880px}
.side h3{position:absolute;font-weight:400;font-size:11.5px;color:#333}
.side-search{left:140px;top:37px;width:108px;height:28px;border:1px solid #ccc;font-size:11px;color:#888;padding:6px 0 0 24px}
.side-search svg{position:absolute;left:9px;top:9px}
.rule{left:0;width:264px;height:1px;background:var(--line)}
.filter{left:0;width:264px;height:24px;background:#f7f7f7;border-bottom:1px solid #eaeaea;font-size:9px;color:#777;padding:6px 0 0 158px}
.filter.active{background:#eef4f7;color:var(--link)}
.show-all{left:158px;top:202px;font-size:9px;color:#777;text-decoration:underline}
.feed-item{right:16px;font-size:9px;color:#777;white-space:nowrap;text-align:right}
.feed-item u{color:#777}
.feed-row{left:0;width:264px;height:1px;background:#e6e6e6}
/* main */
.crumb-title{left:290px;top:92px;font-size:15px;color:#222}
.crumbs{left:386px;top:97px;font-size:9px;color:#777}
.card{left:286px;top:122px;width:602px;height:934px;background:var(--panel);border:1px solid #d5d5d5;border-radius:2px}
.tab{top:0;height:76px;font-size:14.5px;color:#333;display:flex;align-items:center}
.tab.off{background:var(--tab);border-left:1px solid #dde3e6;border-bottom:1px solid #dde3e6}
.tab.create{background:linear-gradient(#7bb12e,var(--green-dark));color:#fff;justify-content:center}
.tab small{font-size:9px;color:#777;margin-left:10px}
.post{left:31px;width:540px}
.avatar{left:0;top:0;width:30px;height:30px;background:linear-gradient(135deg,#e0b08d,#9a5c3c);border:1px solid #ccc;border-radius:2px}
.bubble{left:54px;top:0;width:483px;height:87px;background:var(--bubble);border:1px solid #e4e4e4;border-radius:2px;padding:8px 14px}
.bubble:before{content:"";position:absolute;left:-6px;top:16px;width:10px;height:10px;background:var(--bubble);border-left:1px solid #e4e4e4;border-bottom:1px solid #e4e4e4;transform:rotate(45deg)}
.bubble h2{font-weight:400;font-size:15px;color:#222;display:inline}
.meta{font-size:7px;color:#777;margin-left:6px}
.bubble p{font-size:9.2px;line-height:14.4px;color:#888;margin-top:4px}
.actions{left:55px;top:96px;width:482px;font-size:9.8px;color:var(--soft)}
.actions .right{position:absolute;right:0;top:0;display:flex;gap:22px}
.actions span.i{display:inline-flex;align-items:center;gap:4px}
.msg{left:55px;top:125px;width:420px;height:25px;border:1px solid #ccc;font-size:10.5px;color:#777;padding:5px 0 0 9px}
.send{left:487px;top:125px;width:49px;height:26px;background:linear-gradient(#5aa2bd,var(--send));color:#fff;font-size:11px;text-align:center;line-height:26px;border-radius:2px}
.dots{left:31px;width:536px;height:3px;border-top:1px dotted #aaa;border-bottom:1px dotted #aaa}
</style>
</head>
<body>
<header class="abs topbar">
  <div class="abs sep" style="left:176px"></div>
  <div class="abs sep" style="left:652px"></div>
  <div class="abs sep" style="left:718px"></div>
  <svg class="abs menu" width="14" height="12" viewBox="0 0 14 12"><rect width="14" height="2" fill="#fff"/><rect y="5" width="14" height="2" fill="#fff"/><rect y="10" width="14" height="2" fill="#fff"/></svg>
  <div class="abs logo">Logo</div>
  <div class="abs search"><svg width="10" height="10" viewBox="0 0 10 10"><circle cx="4" cy="4" r="3" fill="none" stroke="#555" stroke-width="1.5"/><line x1="6" y1="6" x2="9.5" y2="9.5" stroke="#555" stroke-width="1.8"/></svg>#acmecorp &nbsp;#globex</div>
  <svg class="abs notify" width="14" height="14" viewBox="0 0 14 14"><circle cx="7" cy="4" r="3" fill="#fff"/><path d="M1 13c0-4 3-5 6-5s6 1 6 5z" fill="#fff"/></svg>
  <div class="abs badge">10</div>
  <div class="abs me-avatar" role="img" aria-label="Profile photo of the signed-in user"></div>
  <div class="abs me-name">Alex Moran</div>
  <div class="abs me-mail">alexmoran@example.com</div>
  <svg class="abs caret" width="8" height="5" viewBox="0 0 8 5"><path d="M0 0l4 4 4-4" stroke="#fff" stroke-width="1.5" fill="none"/></svg>
</header>

<aside class="abs side side-top">
  <svg class="abs" style="left:142px;top:18px" width="10" height="11" viewBox="0 0 10 11"><circle cx="5" cy="3" r="2.8" fill="#444"/><path d="M0 11c0-4 2-5 5-5s5 1 5 5z" fill="#444"/></svg>
  <h3 style="left:161px;top:17px">Users</h3>
  <div class="abs side-search"><svg width="10" height="10" viewBox="0 0 10 10"><circle cx="4" cy="4" r="3" fill="none" stroke="#555" stroke-width="1.5"/><line x1="6" y1="6" x2="9.5" y2="9.5" stroke="#555" stroke-width="1.8"/></svg>Search ...</div>
  <div class="abs rule" style="top:79px"></div>
  <svg class="abs" style="left:140px;top:99px" width="9" height="10" viewBox="0 0 9 10"><path d="M0 0h9L5.5 5v5l-2-1V5z" fill="#333"/></svg>
  <h3 style="left:156px;top:96px">Saved Filters</h3>
  <div class="abs rule" style="top:119px"></div>
  <div class="abs filter" style="top:120px">Filter Item</div>
  <div class="abs filter active" style="top:144px">Filter Item <svg width="9" height="9" viewBox="0 0 10 10" style="margin-left:3px"><path d="M5 0l1.5 3.3 3.5.4-2.6 2.4.7 3.5L5 7.9 1.9 9.6l.7-3.5L0 3.7l3.5-.4z" fill="var(--link)"/></svg></div>
  <div class="abs filter" style="top:168px">Filter Item</div>
  <div class="abs show-all">Show All</div>
</aside>

<aside class="abs side side-feed">
  <div class="abs feed-item" style="top:16px"><u>User X</u> started following <u>User Y</u></div>
  <div class="abs feed-row" style="top:31px"></div>
  <div class="abs feed-item" style="top:40px"><u>User X</u> contributed in discussion <u>'Subject of thread'</u></div>
  <div class="abs feed-row" style="top:55px"></div>
  <div class="abs feed-item" style="top:64px"><u>User X</u> added <u>User Z</u> as a contact</div>
  <div class="abs feed-row" style="top:79px"></div>
  <div class="abs feed-item" style="top:91px">Follow us to receive updates <svg width="9" height="9" viewBox="0 0 10 10" style="margin-left:3px"><path d="M5 .5l1.4 3 3.2.4-2.4 2.2.6 3.2L5 7.8 2.2 9.3l.6-3.2L.4 3.9l3.2-.4z" fill="none" stroke="var(--star)"/></svg></div>
  <div class="abs feed-row" style="top:106px"></div>
  <div class="abs feed-item" style="top:115px">Use these tags to discuss Topic X <svg width="9" height="9" viewBox="0 0 10 10" style="margin-left:3px"><path d="M5 .5l1.4 3 3.2.4-2.4 2.2.6 3.2L5 7.8 2.2 9.3l.6-3.2L.4 3.9l3.2-.4z" fill="none" stroke="var(--star)"/></svg></div>
  <div class="abs feed-row" style="top:130px"></div>
  <div class="abs feed-item" style="top:139px">Filter on this tag to find all our analyses <svg width="9" height="9" viewBox="0 0 10 10" style="margin-left:3px"><path d="M5 .5l1.4 3 3.2.4-2.4 2.2.6 3.2L5 7.8 2.2 9.3l.6-3.2L.4 3.9l3.2-.4z" fill="none" stroke="var(--star)"/></svg></div>
  <div class="abs feed-row" style="top:154px"></div>
</aside>

<svg class="abs" style="left:290px;top:95px" width="14" height="11" viewBox="0 0 14 11"><ellipse cx="8" cy="4.5" rx="6" ry="4.5" fill="#222"/><path d="M2 11l2-4 3 2z" fill="#222"/></svg>
<div class="abs crumb-title" style="left:309px">#acmecorp</div>
<div class="abs crumbs">Home &nbsp;/&nbsp; Conversations &nbsp;/&nbsp; Public &nbsp;/&nbsp; #acmecorp</div>

<main class="abs card">
  <div class="abs tab" style="left:0;width:168px;padding-left:32px">
    <svg width="16" height="16" viewBox="0 0 16 16" style="margin-right:6px"><circle cx="8" cy="8" r="8" fill="var(--badge)"/><path d="M4 5c2 0 3 2 2 4s1 3 1 5M11 3c-1 2 1 3 3 3" stroke="#fff" stroke-width="1.2" fill="none"/></svg>Public<small>Recent &#9662;</small>
  </div>
  <div class="abs tab off" style="left:168px;width:137px;padding-left:26px">
    <svg width="16" height="16" viewBox="0 0 16 16" style="margin-right:10px"><circle cx="4" cy="4" r="3" fill="#c8cfd3"/><circle cx="11" cy="8" r="3" fill="#c8cfd3"/><circle cx="4" cy="12" r="3" fill="#c8cfd3"/></svg>Following
  </div>
  <div class="abs tab off" style="left:305px;width:130px;padding-left:20px">
    <svg width="20" height="16" viewBox="0 0 20 16" style="margin-right:6px"><circle cx="8" cy="5" r="4" fill="#c8cfd3"/><path d="M0 16c0-5 3-6 8-6s8 1 8 6z" fill="#c8cfd3"/><rect x="14" y="9" width="6" height="6" fill="#b5bec3"/></svg>Contacts
  </div>
  <div class="abs tab create" style="left:435px;width:167px">Create Thread <svg width="11" height="11" viewBox="0 0 11 11" style="margin-left:7px"><rect x="4" width="3" height="11" fill="#fff"/><rect y="4" width="11" height="3" fill="#fff"/></svg></div>

  <!-- thread list -->
  <div class="abs post" style="top:107px">
    <div class="abs avatar" role="img" aria-label="Author avatar photo"></div>
    <div class="abs bubble"><h2>What do you think of Skyline OS 8?</h2><span class="meta">Posted by Alex Moran &nbsp;|&nbsp; May 27, 2013 / 09:32 am</span>
      <p>Lorem ipsum dolor sit amet, consectetuer adipiscing elit, sed diam nonummy nibh euismod tincidunt ut laoreet dolore magna aliquam. Lorem ipsum dolor sit amet, consectetuer adipiscing elit, sed diam non-ummy nibh euismod tincidunt ut laoreet dolore magna aliquam.</p></div>
    <div class="abs actions">Read More &nbsp;&nbsp;| &nbsp;&nbsp;12 replies &nbsp;| &nbsp;25 comments
      <div class="right"><span class="i"><svg width="11" height="9" viewBox="0 0 11 9"><ellipse cx="6" cy="4" rx="4.5" ry="3.5" fill="none" stroke="#aaa"/><path d="M1 9l2-3" stroke="#aaa"/></svg>Reply</span><span class="i"><svg width="10" height="9" viewBox="0 0 10 9"><path d="M1 3v5h7V6M4 5l5-4M6 1h3v3" fill="none" stroke="#aaa"/></svg>Share</span><span class="i"><svg width="11" height="9" viewBox="0 0 11 10"><path d="M5.5 9L1 4.5a2.4 2.4 0 014.5-2.5 2.4 2.4 0 014.5 2.5z" fill="none" stroke="#aaa"/></svg>Favorite</span></div></div>
    <div class="abs msg">Enter your message ...</div>
    <div class="abs send">Send</div>
  </div>
  <div class="abs dots" style="top:283px"></div>

  <div class="abs post" style="top:310px">
    <div class="abs avatar" role="img" aria-label="Author avatar photo"></div>
    <div class="abs bubble"><h2>What do you think of Skyline OS 8?</h2><span class="meta">Posted by Alex Moran &nbsp;|&nbsp; May 27, 2013 / 09:32 am</span>
      <p>Lorem ipsum dolor sit amet, consectetuer adipiscing elit, sed diam nonummy nibh euismod tincidunt ut laoreet dolore magna aliquam. Lorem ipsum dolor sit amet, consectetuer adipiscing elit, sed diam non-ummy nibh euismod tincidunt ut laoreet dolore magna aliquam.</p></div>
    <div class="abs actions">Read More &nbsp;&nbsp;| &nbsp;&nbsp;12 replies &nbsp;| &nbsp;25 comments
      <div class="right"><span class="i"><svg width="11" height="9" viewBox="0 0 11 9"><ellipse cx="6" cy="4" rx="4.5" ry="3.5" fill="none" stroke="#aaa"/><path d="M1 9l2-3" stroke="#aaa"/></svg>Reply</span><span class="i"><svg width="10" height="9" viewBox="0 0 10 9"><path d="M1 3v5h7V6M4 5l5-4M6 1h3v3" fill="none" stroke="#aaa"/></svg>Share</span><span class="i"><svg width="11" height="9" viewBox="0 0 11 10"><path d="M5.5 9L1 4.5a2.4 2.4 0 014.5-2.5 2.4 2.4 0 014.5 2.5z" fill="none" stroke="#aaa"/></svg>Favorite</span></div></div>
    <div class="abs msg">Enter your message ...</div>
    <div class="abs send">Send</div>
  </div>
  <div class="abs dots" style="top:486px"></div>

  <div class="abs post" style="top:515px">
    <div class="abs avatar" role="img" aria-label="Author avatar photo"></div>
    <div class="abs bubble"><h2>What do you think of Skyline OS 8?</h2><span class="meta">Posted by Alex Moran &nbsp;|&nbsp; May 27, 2013 / 09:32 am</span>
      <p>Lorem ipsum dolor sit amet, consectetuer adipiscing elit, sed diam nonummy nibh euismod tincidunt ut laoreet dolore magna aliquam. Lorem ipsum dolor sit amet, consectetuer adipiscing elit, sed diam non-ummy nibh euismod tincidunt ut laoreet dolore magna aliquam.</p></div>
    <div class="abs actions">Read More &nbsp;&nbsp;| &nbsp;&nbsp;12 replies &nbsp;| &nbsp;25 comments
      <div class="right"><span class="i"><svg width="11" height="9" viewBox="0 0 11 9"><ellipse cx="6" cy="4" rx="4.5" ry="3.5" fill="none" stroke="#aaa"/><path d="M1 9l2-3" stroke="#aaa"/></svg>Reply</span><span class="i"><svg width="10" height="9" viewBox="0 0 10 9"><path d="M1 3v5h7V6M4 5l5-4M6 1h3v3" fill="none" stroke="#aaa"/></svg>Share</span><span class="i"><svg width="11" height="9" viewBox="0 0 11 10"><path d="M5.5 9L1 4.5a2.4 2.4 0 014.5-2.5 2.4 2.4 0 014.5 2.5z" fill="none" stroke="#aaa"/></svg>Favorite</span></div></div>
    <div class="abs msg">Enter your message ...</div>
    <div class="abs send">Send</div>
  </div>
  <div class="abs dots" style="top:691px"></div>

  <div class="abs post" style="top:718px">
    <div class="abs avatar" role="img" aria-label="Author avatar photo"></div>
    <div class="abs bubble"><h2>What do you think of Skyline OS 8?</h2><span class="meta">Posted by Alex Moran &nbsp;|&nbsp; May 27, 2013 / 09:32 am</span>
      <p>Lorem ipsum dolor sit amet, consectetuer adipiscing elit, sed diam nonummy nibh euismod tincidunt ut laoreet dolore magna aliquam. Lorem ipsum dolor sit amet, consectetuer adipiscing elit, sed diam non-ummy nibh euismod tincidunt ut laoreet dolore magna aliquam.</p></div>
    <div class="abs actions">Read More &nbsp;&nbsp;| &nbsp;&nbsp;12 replies &nbsp;| &nbsp;25 comments
      <div class="right"><span class="i"><svg width="11" height="9" viewBox="0 0 11 9"><ellipse cx="6" cy="4" rx="4.5" ry="3.5" fill="none" stroke="#aaa"/><path d="M1 9l2-3" stroke="#aaa"/></svg>Reply</span><span class="i"><svg width="10" height="9" viewBox="0 0 10 9"><path d="M1 3v5h7V6M4 5l5-4M6 1h3v3" fill="none" stroke="#aaa"/></svg>Share</span><span class="i"><svg width="11" height="9" viewBox="0 0 11 10"><path d="M5.5 9L1 4.5a2.4 2.4 0 014.5-2.5 2.4 2.4 0 014.5 2.5z" fill="none" stroke="#aaa"/></svg>Favorite</span></div></div>
    <div class="abs msg">Enter your message ...</div>
    <div class="abs send">Send</div>
  </div>
  <div class="abs dots" style="top:894px"></div>
</main>
</body>
</html>
```